Honigetikett gesucht
Zielgruppe
Ich bin ein Hobbyimker und brauche ein Etikett für meinen Honig. Zielgruppe = Jeder
Aufgabenstellung
Bitte keine schwarzen Etiketten mehr... gefällt uns leider nicht. Danke!
Das Etikett ist für Honig, 500 Gramm Glas. Man muss den gesetzlichen Vorgaben einhalten. https://www.wabenhof-vorlu.at/de/labor/lebensmittelrecht.html
Blütenhonig aus Österreich
Name
Adresse
500 g
Trocken und vor Licht und Wärme geschützt lagern.
Mindestens haltbar bis:
Sichtfeldregelung
Sachbezeichnung und Nettofüllmenge müssen am Etikett in einem Sichtfeld angebracht werden. Ein Sichtfeld ist eine Oberfläche einer Verpackung, die von einem einzigen Blickpunkt aus gelesen werden kann.
Mindesthaltbarkeitsdatum und Lagerbedingungen sind in einem Sichtfeld anzubringen. Dabei muss die Lagerbedingung über oder unter der Haltbarkeit angeführt werden und darf nicht durch Bild- oder Schrift getrennt sein.
Mindestschriftgröße aller verpflichtenden Angaben (Ausnahme Nettofüllmenge) Mindestschriftgröße:
Die verwendete Schrift muss am kleinen „x“ der verwendeten Schriftart gemessen mindestens 1,2mm Höhe ausmachen
Erreicht die Gesamtoberfläche des Gebindes auf dem Ein Etikett angebracht werden kann max. 80cm2, so muss die Höhe am kleinen „x“ der verwendeten Schriftart gemessen mindestens 0,9mm Höhe ausmachen (beim Honigglas wäre dies erst unter dem 125g Glas)
Die Mindestschriftgröße der Nettofüllmenge bleibt davon unberührt und unterliegt weiterhin der Fertigpackungsverordnung (siehe Nettofüllmenge)

```html
<!DOCTYPE html>
<html lang="de">
<head>
<meta charset="utf-8">
<title>Blütenhonig Etikett</title>
<link rel="stylesheet" href="https://fonts.googleapis.com/css2?family=Mrs+Saint+Delafield&family=Pathway+Gothic+One&family=Open+Sans:wght@700&display=swap">
<style>
  :root {
    --page: #ffffff;
    --kraft: #f6e2c6;
    --kraft-light: #fbeedd;
    --ink: #1d1a17;
    --tone-pink: rgba(238, 143, 176, 0.55);
    --tone-red: rgba(226, 69, 110, 0.5);
    --tone-purple: rgba(157, 135, 210, 0.5);
    --tone-orange: rgba(246, 192, 106, 0.55);
    --tone-leaf: rgba(37, 144, 124, 0.5);
    --tone-bee: rgba(242, 168, 31, 0.45);
    --tone-berry: rgba(226, 69, 110, 0.3);
    --date-box: #ffffff;
  }
  * { margin: 0; padding: 0; box-sizing: border-box; }
  html, body {
    width: 1200px; height: 1200px; overflow: hidden;
    background: var(--page);
  }
  .canvas { position: relative; width: 1200px; height: 1200px; }
  .label {
    position: absolute; left: 40px; top: 423px;
    width: 1120px; height: 353px; overflow: hidden;
    background: radial-gradient(ellipse at 52% 62%, var(--kraft-light) 0%, var(--kraft) 60%);
    color: var(--ink);
  }

  /* illustration areas: single soft tone fading into the kraft paper */
  .art { position: absolute; background: radial-gradient(closest-side, var(--tone) 0%, transparent 100%); }
  .art--leaf-cluster   { --tone: var(--tone-red);    left: -40px; top: -40px; width: 200px; height: 210px; }
  .art--pink-flower    { --tone: var(--tone-pink);   left: 178px; top: 36px;  width: 121px; height: 121px; }
  .art--tulip          { --tone: var(--tone-orange); left: 170px; top: 175px; width: 100px; height: 110px; }
  .art--red-flower     { --tone: var(--tone-red);    left: 334px; top: 222px; width: 120px; height: 115px; }
  .art--pink-flower-r  { --tone: var(--tone-pink);   left: 652px; top: 236px; width: 100px; height: 95px; }
  .art--purple-flower-m{ --tone: var(--tone-purple); left: 766px; top: 170px; width: 112px; height: 106px; }
  .art--purple-flower-t{ --tone: var(--tone-purple); left: 936px; top: 28px;  width: 106px; height: 94px; }
  .art--berry-sprig    { --tone: var(--tone-berry);  left: 640px; top: -30px; width: 130px; height: 70px; }
  .art--bee            { --tone: var(--tone-bee);    left: 780px; top: 30px;  width: 120px; height: 124px; }
  .art--leaves-corner  { --tone: var(--tone-leaf);   left: 1000px; top: 240px; width: 200px; height: 180px; }

  .title {
    position: absolute; left: 300px; top: 34px; width: 500px; text-align: center;
    font-family: "Mrs Saint Delafield", cursive; font-size: 150px; line-height: 1;
    font-weight: 400; color: var(--ink); white-space: nowrap;
  }
  .origin {
    position: absolute; left: 400px; top: 180px; width: 320px; text-align: center;
    font-family: "Pathway Gothic One", sans-serif; font-size: 48px; line-height: 1;
  }
  .net-weight {
    position: absolute; left: 460px; top: 292px; width: 200px; text-align: center;
    font-family: "Open Sans", sans-serif; font-weight: 700; font-size: 38px; line-height: 1;
  }
  .producer {
    position: absolute; left: 21px; top: 199px;
    font-family: "Pathway Gothic One", sans-serif; font-size: 21px; line-height: 28px;
    font-style: normal;
  }
  .producer .email { margin-top: 14px; display: block; }
  .storage {
    position: absolute; left: 902px; top: 155px; width: 210px;
    font-family: "Pathway Gothic One", sans-serif; font-size: 21px; line-height: 24px;
  }
  .storage .best-before { margin-top: 30px; }
  .date-field {
    position: absolute; left: 902px; top: 272px; width: 186px; height: 45px;
    background: var(--date-box);
  }
</style>
</head>
<body>
<main class="canvas">
  <section class="label" aria-label="Honigetikett Blütenhonig">
    <div class="art art--leaf-cluster" role="img" aria-label="Illustration: rote Blüte mit grünen Blättern"></div>
    <div class="art art--pink-flower" role="img" aria-label="Illustration: rosa Blüte"></div>
    <div class="art art--tulip" role="img" aria-label="Illustration: orange Tulpenblüte"></div>
    <div class="art art--red-flower" role="img" aria-label="Illustration: rote Blüte"></div>
    <div class="art art--pink-flower-r" role="img" aria-label="Illustration: rosa Blüte"></div>
    <div class="art art--purple-flower-m" role="img" aria-label="Illustration: violette Blüte"></div>
    <div class="art art--purple-flower-t" role="img" aria-label="Illustration: violette Blüte"></div>
    <div class="art art--berry-sprig" role="img" aria-label="Illustration: Beerenzweig"></div>
    <div class="art art--bee" role="img" aria-label="Illustration: Biene mit Honigeimer"></div>
    <div class="art art--leaves-corner" role="img" aria-label="Illustration: grüne Blätter"></div>

    <h1 class="title">Blütenhonig</h1>
    <p class="origin">aus Österreich</p>
    <p class="net-weight">500 g</p>

    <address class="producer">
      Hanna Tormel<br>
      Kleefeldgasse 4b<br>
      1220 Wien
      <span class="email">h.tormel77@wabenpost.at</span>
    </address>

    <div class="storage">
      <p>Trocken und vor Licht und Wärme geschützt lagern.</p>
      <p class="best-before">Mindestens haltbar bis:</p>
    </div>
    <div class="date-field"></div>
  </section>
</main>
</body>
</html>
```